Valtimore Sciences needs high end Label Design for a revolutionary new supplement

We at Valtimore Sciences are looking for a brand new Label Design for a first of its kind product called Tolmisse. It is the first supplement on the market that treats grief and heartbreak. This product is unisex for both men and woman. We want the New Label to look high end and luxurious using the brand colors which are gold and burgundy. Please feel free to use other colors such as black, white, or gray to go along with it or any other colors if you feel would be a great fit! Valtimore Sciences is like the Quorvel of the supplement world, coming out with new products that will challenge the way people treat different symptoms. To Recap:

1. Product Name: TOLMISSE - the font will play a big roll
2. The Label will be placed on an all white bottle
3. Some parts of the label will be printed with foil to make parts of the label shiny and more attractive. Please keep this in mind when designing.
4. Must use our Logo. I will attach a file of our logo and of the emblem as well. Feel free to use the emblem separately if you have a great idea for it. Please let us know if you need the Logo in a different file type.
5. This all natural herbal supplement in pill form is the first to treat grief and support someone with a broken heart. The consumers purchasing this product will be going through a hard and emotional time. This is a serious product.
6. The manufacturer has included some basic instructions regarding the dye line and file types. Please do your best to meet these. If you cannot meet the guidelines please submit art work anyways. If your design is chosen we will just have the manufacturer replicate the design.

The final label should portray Tolmisse and Valtimore Sciences as a luxurious brand and product which was made with cutting edge science leading the way with revolutionary ideas. We want customers to feel that the product is worth every penny, because it is. As soon as they receive the product and take one look at the label, I want them to think WOW I made the right choice buying this. I have attached some Label designs that we really liked for your review.

Please feel free to message me with any questions or if you need the Logo in a different file type. Thank you all.
Updates

Please send in more entries while we take a couple days to review, we are still looking for that one design we can work with. We are getting close, thank you all!

Target Market(s)

People going through grief and heartbreak.

Font styles to use
Sans Serif
Script
Other font styles liked:
• Any font that looks good, The font for the name TOLMISSE is very important and will brand it. We hated the font used in the label we received in our first label draft (attached so you can see)

Requirements
Must have
• Must have the company Logo that says the company name
• Must have the colors Gold and Burgundy
• Must have some areas that will be the shiny foil when label is printed.
• Must say "Dietary Supplement" somewhere near the bottom along with "90 Capsules"
• I have attached a Label someone designed for us but were not really happy with. I did like the font the "Dietary supplement" and "90 Capsules" had and also where it was placed. We absolutely HATED the font used for Tolmisse.
• Must look at the label design we received from the manufacturer and take into consideration the room needed to write in the directions and all the symbols such as "made in america" and "BQH Facility" Don't worry about adding these in as they will put those in before printing but keep in mind they will be added to the Final Label along with the Supplement Facts.
Nice to have
• Would like to see other colors to go with gold and burgundy suck as black, white, or gray. I have attached some Label designs that I really liked for your reference.
Should not have
• Does not need to have any other legal language, that will be applied by the the manufacturer's graphics team.

```html
<!DOCTYPE html>
<html lang="en">
<head>
<meta charset="utf-8">
<title>Tolmisse Label Concepts – Valtimore Sciences</title>
<link rel="stylesheet" href="https://fonts.googleapis.com/css2?family=Cinzel:wght@500&family=Montserrat:wght@500;700&family=Playfair+Display:wght@400&family=Pinyon+Script&display=swap">
<style>
  :root {
    --page: #ffffff;
    --burgundy-deep: #3a1414;
    --burgundy-mid: #5e1d1e;
    --gold-dark: #9c6b1c;
    --gold-light: #f6dc86;
    --gold: #d4a445;
    --brand-red: #c42a2a;
  }
  html, body {
    margin: 0;
    width: 1200px;
    height: 1200px;
    overflow: hidden;
    background: var(--page);
  }
  .canvas {
    position: relative;
    width: 1200px;
    height: 1200px;
  }
  .label {
    position: absolute;
    width: 364px;
    height: 412px;
    box-shadow: 0 10px 30px rgba(0,0,0,0.18);
  }
  .label--classic { left: 376px; top: 152px; }
  .label--ornate  { left: 84px;  top: 680px; }
  .label--accent  { left: 764px; top: 572px; }

  .label-bg-stop-edge { stop-color: var(--burgundy-deep); }
  .label-bg-stop-core { stop-color: var(--burgundy-mid); }
  .foil-stop-dark  { stop-color: var(--gold-dark); }
  .foil-stop-light { stop-color: var(--gold-light); }
  .band-stop-a { stop-color: var(--gold-dark); }
  .band-stop-b { stop-color: var(--gold); }

  .foil-line { fill: none; stroke: url(#foil); stroke-width: 4; }
  .foil-line--thin { stroke-width: 2.5; }
  .ornament-band { fill: url(#band); opacity: 0.85; }
  .arch-fill { fill: url(#labelBg); }

  .brand-mark { fill: none; stroke: var(--brand-red); stroke-width: 3; }
  .brand-name {
    font-family: "Cinzel", serif;
    font-weight: 500;
    fill: var(--brand-red);
    letter-spacing: 4px;
  }
  .product-name--sans {
    font-family: "Montserrat", sans-serif;
    font-weight: 700;
    font-size: 80px;
    fill: url(#foil);
  }
  .product-name--script {
    font-family: "Pinyon Script", cursive;
    font-size: 96px;
    fill: url(#foil);
  }
  .supplement-type {
    font-family: "Montserrat", sans-serif;
    font-weight: 500;
    font-size: 19px;
    letter-spacing: 1px;
    fill: var(--gold);
  }
  .count {
    font-family: "Playfair Display", serif;
    font-size: 52px;
    fill: url(#foil);
  }
  .count-unit {
    font-family: "Montserrat", sans-serif;
    font-weight: 500;
    font-size: 10px;
    fill: var(--gold);
  }
</style>
</head>
<body>
<main class="canvas">

  <!-- Classic sans variant -->
  <svg class="label label--classic" viewBox="0 0 455 515" aria-label="Tolmisse label, sans serif name">
    <defs>
      <radialGradient id="labelBg" cx="50%" cy="50%" r="70%">
        <stop offset="0" class="label-bg-stop-core"/>
        <stop offset="1" class="label-bg-stop-edge"/>
      </radialGradient>
      <linearGradient id="foil" x1="0" y1="0" x2="1" y2="1">
        <stop offset="0" class="foil-stop-dark"/>
        <stop offset="0.5" class="foil-stop-light"/>
        <stop offset="1" class="foil-stop-dark"/>
      </linearGradient>
      <linearGradient id="band" x1="0" y1="0" x2="1" y2="0">
        <stop offset="0" class="band-stop-a"/>
        <stop offset="0.5" class="band-stop-b"/>
        <stop offset="1" class="band-stop-a"/>
      </linearGradient>
    </defs>
    <rect width="455" height="515" fill="url(#labelBg)"/>
    <path class="foil-line" d="M0,112 L150,95 C160,60 190,32 228,32 C266,32 296,60 306,95 L455,112"/>
    <circle class="brand-mark" cx="228" cy="95" r="22"/>
    <text class="brand-name" x="228" y="165" text-anchor="middle" font-size="22">VALTIMORE</text>
    <text class="brand-name" x="228" y="186" text-anchor="middle" font-size="17">SCIENCES</text>
    <text class="product-name--sans" x="228" y="300" text-anchor="middle">Tolmisse</text>
    <text class="supplement-type" x="228" y="385" text-anchor="middle">FOOD ADDITIVE</text>
    <path class="foil-line" d="M0,418 L140,410 C152,468 190,490 228,490 C266,490 304,468 316,410 L455,418"/>
    <path class="foil-line foil-line--thin" d="M0,428 L148,420 C160,475 195,500 228,500 C262,500 296,475 308,420 L455,428"/>
    <text class="count" x="228" y="440" text-anchor="middle">90</text>
    <text class="count-unit" x="228" y="456" text-anchor="middle">CAPSULES</text>
  </svg>

  <!-- Ornate script variant -->
  <svg class="label label--ornate" viewBox="0 0 455 515" aria-label="Tolmisse label, script name with ornament bands">
    <rect width="455" height="515" fill="url(#labelBg)"/>
    <rect class="ornament-band" x="0" y="12" width="455" height="52" role="img" aria-label="Gold foil swirl ornament band"/>
    <path class="arch-fill" d="M130,100 C145,50 185,22 228,22 C271,22 311,50 326,100 Z"/>
    <path class="foil-line" d="M0,98 L140,86 C152,46 190,22 228,22 C266,22 304,46 316,86 L455,98"/>
    <path class="foil-line foil-line--thin" d="M0,110 L150,98 C162,62 195,38 228,38 C261,38 294,62 306,98 L455,110"/>
    <circle class="brand-mark" cx="228" cy="95" r="22"/>
    <text class="brand-name" x="228" y="165" text-anchor="middle" font-size="22">VALTIMORE</text>
    <text class="brand-name" x="228" y="186" text-anchor="middle" font-size="17">SCIENCES</text>
    <text class="product-name--script" x="228" y="300" text-anchor="middle">Tolmisse</text>
    <text class="supplement-type" x="228" y="385" text-anchor="middle">FOOD ADDITIVE</text>
    <rect class="ornament-band" x="0" y="430" width="455" height="62" role="img" aria-label="Gold foil swirl ornament band"/>
    <path class="arch-fill" d="M140,412 C152,470 190,494 228,494 C266,494 304,470 316,412 Z"/>
    <path class="foil-line" d="M0,408 L140,402 C152,462 190,486 228,486 C266,486 304,462 316,402 L455,408"/>
    <path class="foil-line foil-line--thin" d="M0,420 L148,414 C160,470 195,496 228,496 C262,496 296,470 308,414 L455,420"/>
    <text class="count" x="228" y="440" text-anchor="middle">90</text>
    <text class="count-unit" x="228" y="456" text-anchor="middle">CAPSULES</text>
  </svg>

  <!-- Accent script variant -->
  <svg class="label label--accent" viewBox="0 0 455 515" aria-label="Tolmisse label, script name with lower ornament band">
    <rect width="455" height="515" fill="url(#labelBg)"/>
    <path class="foil-line" d="M0,112 L150,95 C160,60 190,32 228,32 C266,32 296,60 306,95 L455,112"/>
    <circle class="brand-mark" cx="228" cy="95" r="22"/>
    <text class="brand-name" x="228" y="165" text-anchor="middle" font-size="22">VALTIMORE</text>
    <text class="brand-name" x="228" y="186" text-anchor="middle" font-size="17">SCIENCES</text>
    <text class="product-name--script" x="228" y="300" text-anchor="middle">Tolmisse</text>
    <text class="supplement-type" x="228" y="385" text-anchor="middle">FOOD ADDITIVE</text>
    <rect class="ornament-band" x="0" y="432" width="455" height="66" role="img" aria-label="Gold foil swirl ornament band"/>
    <path class="arch-fill" d="M140,412 C152,470 190,494 228,494 C266,494 304,470 316,412 Z"/>
    <path class="foil-line" d="M0,412 L140,406 C152,464 190,488 228,488 C266,488 304,464 316,406 L455,412"/>
    <path class="foil-line foil-line--thin" d="M0,424 L148,418 C160,472 195,498 228,498 C262,498 296,472 308,418 L455,424"/>
    <text class="count" x="228" y="440" text-anchor="middle">90</text>
    <text class="count-unit" x="228" y="456" text-anchor="middle">CAPSULES</text>
  </svg>

</main>
</body>
</html>
```